i am creating an a new cold brew coffee and need a standard format for 5 different flavours. the PDF with 5 colours is what i created as a format and the one page PDF is the style i like but am happy yo move away from it.. the images are the style i like

i am looking for a nice clean tidy but standard out label that will pop off a brown paper backing.

Target Market(s)

18-40 Yr old coffee lovers wanting a high end cold brew coffee

Font styles to use
Serif
Sans Serif

Colors

Designer to choose colors to be used in the design.

Requirements
Must have
• i want a standard format that a component can change colour with flavours, brown paper background. i need the nutritional content box at the back ( as per PDF ) and i would like the text added also, as this is a description of the product
Nice to have
• i like the tidy clinical look of the font pharma bold condensed
• the PDF's show the flavours.. the one with a brown background is something i have seen that i like and the images are the styles i like .

```html
<!DOCTYPE html>
<html lang="en">
<head>
<meta charset="utf-8">
<title>Harbour Brews – Sparkling Ginger Label</title>
<link href="https://fonts.googleapis.com/css2?family=Antonio:wght@700&family=Oswald:wght@600&family=Rubik:wght@400;500&family=Roboto+Slab:wght@500;700&display=swap" rel="stylesheet">
<style>
  :root {
    --kraft: #d4ad7e;
    --kraft-light: #dcb98c;
    --kraft-dark: #c99f6e;
    --brown: #5a3418;
    --brown-ink: #4d2c12;
    --flavour: #a3c044;
    --gold-a: #b8861f;
    --gold-b: #f3d36a;
    --white: #ffffff;
  }
  * { margin: 0; padding: 0; box-sizing: border-box; }
  html, body { width: 1200px; height: 630px; overflow: hidden; background: var(--white); }
  body { position: relative; font-family: "Rubik", Arial, sans-serif; color: var(--brown-ink); }

  .label { position: absolute; left: 156px; top: 100px; width: 888px; height: 412px; }
  .panel { position: absolute; top: 0; height: 100%; }
  .panel--back, .panel--story {
    width: 336px;
    background: radial-gradient(circle at 30% 40%, var(--kraft-light), var(--kraft) 55%, var(--kraft-dark));
  }
  .panel--back { left: 0; }
  .panel--front { left: 336px; width: 216px; background: var(--brown); overflow: hidden; }
  .panel--story { left: 552px; }

  /* Nutrition table */
  .nutrition { position: absolute; left: 38px; top: 24px; width: 215px; height: 254px;
    border: 2px solid var(--brown); border-radius: 7px; overflow: hidden; }
  .nutrition__head { background: var(--brown); color: var(--white); height: 27px;
    font-size: 15px; line-height: 27px; padding-left: 8px; letter-spacing: .2px; }
  .nutrition__meta { position: relative; font-size: 8.5px; font-weight: 500; line-height: 12px; padding: 10px 7px 0; height: 44px; }
  .nutrition__cols { position: absolute; top: 8px; right: 8px; display: flex; gap: 22px; line-height: 9px; }
  .nutrition__rows { list-style: none; padding: 0 7px; }
  .nutrition__rows li { height: 20px; border-bottom: 1px solid var(--brown); font-size: 13px; line-height: 20px; }
  .nutrition__rows li.sub { padding-left: 9px; }
  .nutrition__ingredients { font-size: 8.5px; line-height: 11px; padding: 6px 7px 0; }
  .care { position: absolute; left: 46px; top: 286px; font-size: 8.5px; font-weight: 500; line-height: 11.5px; }
  .badge { position: absolute; top: 333px; width: 64px; text-align: center; font-size: 7.5px; font-weight: 500; line-height: 8px; }
  .badge__mark { display: block; margin: 0 auto 2px; width: 39px; height: 39px; border-radius: 50%; border: 3px solid var(--brown); }
  .badge--gf { left: 135px; }
  .badge--vegan { left: 199px; }

  /* Front card */
  .front-card { position: absolute; left: 6px; top: 26px; }
  .est { position: absolute; left: 0; top: 45px; width: 216px; text-align: center;
    font-family: "Oswald", sans-serif; font-weight: 600; font-size: 8.5px; letter-spacing: .5px; color: var(--brown-ink); }
  .est__dot { display: inline-block; width: 14px; height: 14px; border-radius: 50%; background: var(--brown); vertical-align: middle; margin: 0 8px; }
  .brand-name { position: absolute; left: 0; top: 104px; width: 216px; text-align: center;
    font-family: "Antonio", "Oswald", sans-serif; font-weight: 700; font-size: 60px; line-height: 62px; color: var(--brown-ink); letter-spacing: 0; white-space: nowrap; }
  .flavour-tag { position: absolute; left: 45px; top: 271px; width: 126px; height: 18px;
    background: linear-gradient(90deg, var(--gold-a), var(--gold-b) 50%, var(--gold-a));
    font-family: "Roboto Slab", serif; font-weight: 700; font-size: 10px; line-height: 18px; text-align: center; letter-spacing: 1.5px; color: var(--brown-ink); }
  .flavour-name { position: absolute; left: 0; top: 296px; width: 216px; text-align: center;
    font-family: "Roboto Slab", serif; font-weight: 500; font-size: 12px; color: var(--brown-ink); }
  .origin-claim { position: absolute; left: 44px; top: 314px; width: 128px; height: 34px;
    border-top: 1.5px solid var(--brown); border-bottom: 1.5px solid var(--brown);
    display: flex; align-items: center; font-family: "Roboto Slab", serif; color: var(--brown-ink); }
  .origin-claim__pct { font-size: 17px; font-weight: 700; padding-right: 4px; border-right: 1.5px solid var(--brown); line-height: 24px; }
  .origin-claim__text { font-size: 7.5px; line-height: 9px; padding-left: 3px; font-weight: 500; }
  .volume { position: absolute; left: 0; top: 368px; width: 216px; text-align: center;
    font-family: "Roboto Slab", serif; font-weight: 700; font-size: 10px; color: var(--brown-ink); }

  /* Story panel */
  .story { position: absolute; left: 84px; top: 26px; width: 218px; font-size: 11px; line-height: 13.5px; }
  .story p { margin-bottom: 12px; }
  .contact { position: absolute; left: 84px; top: 244px; font-size: 13.5px; font-weight: 500; line-height: 20px; white-space: nowrap; }
  .trade { position: absolute; left: 162px; top: 352px; font-size: 10.5px; line-height: 14px; }
  .refund { position: absolute; left: 310px; top: 24px; width: 21px; height: 364px; border-radius: 8px; background: var(--brown); }
  .refund__text { position: absolute; left: 50%; top: 50%; width: 340px; transform: translate(-50%, -50%) rotate(-90deg);
    color: var(--white); font-size: 10.5px; white-space: nowrap; text-align: left; padding-left: 18px; }
  .refund__text b { font-size: 13px; }
</style>
</head>
<body>
<main class="label">

  <section class="panel panel--back">
    <div class="nutrition">
      <div class="nutrition__head">NUTRITIONAL INFORMATION</div>
      <div class="nutrition__meta">
        Servings: 1<br>Serving: 330ml
        <div class="nutrition__cols"><span>Av.<br>per<br>Serv.</span><span>Av.<br>per<br>100g</span></div>
      </div>
      <ul class="nutrition__rows">
        <li>Energy</li>
        <li>Protein</li>
        <li>Fat, Total</li>
        <li class="sub">Saturated</li>
        <li>Carbs</li>
        <li class="sub">Sugar</li>
        <li>Sodium</li>
      </ul>
      <p class="nutrition__ingredients">All Organic Ingredients:<br>Cold Brew coffee, Arabica Beans, Raw<br>Coconut Nectar, Ginger 4 %</p>
    </div>
    <p class="care">*Keep Refrigerated after opening &amp;<br>consume within 2 days from opening<br>* Please do not shake</p>
    <div class="badge badge--gf"><span class="badge__mark"></span>Gluten<br>Free</div>
    <div class="badge badge--vegan"><span class="badge__mark"></span>Naturally<br>Vegan</div>
  </section>

  <section class="panel panel--front">
    <svg class="front-card" width="204" height="360" viewBox="0 0 204 360" aria-hidden="true">
      <defs>
        <clipPath id="card-shape">
          <path d="M14 0 H190 Q190 10 196 12 Q204 14 204 24 V336 Q204 346 196 348 Q190 350 190 360 H14 Q14 350 8 348 Q0 346 0 336 V24 Q0 14 8 12 Q14 10 14 0 Z"/>
        </clipPath>
      </defs>
      <g clip-path="url(#card-shape)">
        <rect width="204" height="360" fill="var(--kraft)"/>
        <rect y="254" width="204" height="106" fill="var(--flavour)"/>
      </g>
    </svg>
    <div class="est">EST.<span class="est__dot"></span>1000</div>
    <h1 class="brand-name">HARBOUR<br>BREWS</h1>
    <div class="flavour-tag">COFFEE</div>
    <div class="flavour-name">SPARKLING GINGER</div>
    <div class="origin-claim">
      <span class="origin-claim__pct">100%</span>
      <span class="origin-claim__text">AUSTRALIAN<br>MADE &amp; OWNED</span>
    </div>
    <div class="volume">330 ML</div>
  </section>

  <section class="panel panel--story">
    <div class="story">
      <p>Harbour Brews made this Cold brew coffee to make you think clearer, feel motivated and to just be a better person.</p>
      <p>We wont claim any responsibility for the achievements you make while drinking our brews, that brilliance was always about you, we just helped you bring it out.</p>
      <p>We know that if you have finished the bottle you will be feeling too good to be reading this label in its entirety. So we will finish it here so you can continue on your motivated way.</p>
    </div>
    <p class="contact">Want to contact us? Sure do it<br>here: www.harbourbrews.com.au<br>Or here 42 Larkin Street,<br>Ashbury NSW 2193 or on<br>this 0400 123 456</p>
    <p class="trade">World first release:<br>Call 0400 987 654<br>For distribution enquiries.</p>
    <div class="refund"><div class="refund__text"><b>10c</b> refund at collection depots ########</div></div>
  </section>

</main>
</body>
</html>
```